Psychology text book for statistics needs front cover

We need a logo/picture that will be the front cover of our book.

Our book is on person-specific data analysis. Such as: predicting when someone might binge drink, understanding personal processes (e.g., emotional processes; brain processes), or quantifying what depression means for a given individual.

So, something that merges the concept of people as individuals with their own processes (or life path) with statistics would be great.

Target Market(s)

Higher education

Logo Text

Mapping of Tidal Echo Patterns (optional)

Logo styles of interest
Pictorial/Combination Logo
Abstract Logo
Font styles to use
Sans Serif

Requirements
Must have
• The title of the book is:
Mapping of Tidal Echo Patterns: Lantern Methods for Quiet Signal Review

It would be fine to just include the first part - Mapping of Tidal Echo Patterns
Nice to have
• For inspiration: perhaps something that has a clear image of an individual in a crowd where everyone else is blurry. Or on a path. If you could figure out how to meld this together with some image representing data across time (such as lines on a plot see examples), that would be great.

```html
<!DOCTYPE html>
<html lang="en">
<head>
<meta charset="utf-8">
<title>Mapping of Tidal Echo Patterns – Book Cover</title>
<link href="https://fonts.googleapis.com/css2?family=Anton&display=swap" rel="stylesheet">
<style>
  :root {
    --stage-bg: #f2f2f2;
    --earth-dark: #3b2a22;
    --earth-mid: #5e4336;
    --earth-warm: #7a5646;
    --earth-light: #8c6a58;
    --leaf-green: #7fae6a;
    --ink-white: #ffffff;
    --chart-fill: rgba(255, 255, 255, 0.16);
    --chart-grid: rgba(255, 255, 255, 0.28);
  }
  * { box-sizing: border-box; margin: 0; padding: 0; }
  html, body {
    width: 1200px;
    height: 700px;
    overflow: hidden;
    background: var(--stage-bg);
  }
  .stage {
    position: relative;
    width: 1200px;
    height: 700px;
  }
  .book-cover {
    position: absolute;
    left: 367px;
    top: 0;
    width: 466px;
    height: 700px;
    overflow: hidden;
  }
  .cover-photo {
    position: absolute;
    inset: 0;
    background:
      radial-gradient(ellipse 60px 110px at 230px 345px, var(--leaf-green) 0%, rgba(127,174,106,0.55) 45%, rgba(127,174,106,0) 100%),
      radial-gradient(circle at 20% 25%, var(--earth-light) 0%, rgba(140,106,88,0) 35%),
      radial-gradient(circle at 80% 60%, var(--earth-warm) 0%, rgba(122,86,70,0) 40%),
      radial-gradient(circle at 35% 80%, var(--earth-light) 0%, rgba(140,106,88,0) 35%),
      linear-gradient(160deg, var(--earth-mid) 0%, var(--earth-dark) 50%, var(--earth-mid) 100%);
  }
  .cover-chart {
    position: absolute;
    inset: 0;
    width: 466px;
    height: 700px;
  }
  .cover-text {
    position: absolute;
    left: 0;
    right: 0;
    top: 44px;
    text-align: center;
    color: var(--ink-white);
    font-family: 'Anton', 'Impact', sans-serif;
    line-height: 1;
  }
  .author-name {
    font-size: 40px;
    letter-spacing: 0.3px;
  }
  .book-title {
    font-weight: 400;
    margin-top: 12px;
  }
  .title-lead {
    display: block;
    font-size: 62px;
    line-height: 1;
  }
  .title-main {
    display: block;
    font-size: 43px;
    line-height: 1;
    margin-top: 4px;
  }
  .title-subtitle {
    display: block;
    font-size: 21px;
    line-height: 1;
    margin-top: 6px;
    letter-spacing: 0.2px;
  }
</style>
</head>
<body>
<main class="stage">
  <section class="book-cover">
    <div class="cover-photo" role="img" aria-label="Photograph of a forest floor covered in brown fallen leaves with a single green holly leaf in the centre"></div>

    <svg class="cover-chart" viewBox="0 0 466 700" preserveAspectRatio="none" aria-hidden="true">
      <g class="chart-grid" stroke="var(--chart-grid)" stroke-width="1">
        <line x1="12" y1="480" x2="440" y2="480"/>
        <line x1="12" y1="540" x2="440" y2="540"/>
        <line x1="12" y1="600" x2="440" y2="600"/>
      </g>
      <polygon class="chart-area" points="12,660 80,612 160,636 240,560 320,585 400,505 400,660" fill="var(--chart-fill)"/>
      <polyline class="chart-line" points="12,660 80,612 160,636 240,560 320,585 400,505" fill="none" stroke="#ffffff" stroke-width="2.5" stroke-linejoin="round"/>
      <g class="chart-axes" stroke="#ffffff" stroke-width="2.5" fill="none">
        <line x1="12" y1="660" x2="12" y2="440"/>
        <line x1="12" y1="660" x2="448" y2="660"/>
        <line x1="80" y1="655" x2="80" y2="665"/>
        <line x1="160" y1="655" x2="160" y2="665"/>
        <line x1="240" y1="655" x2="240" y2="665"/>
        <line x1="320" y1="655" x2="320" y2="665"/>
        <line x1="400" y1="655" x2="400" y2="665"/>
      </g>
      <g class="chart-arrows" fill="#ffffff">
        <polygon points="12,430 6,443 18,443"/>
        <polygon points="460,660 447,654 447,666"/>
      </g>
      <g class="chart-points" fill="var(--earth-dark)" stroke="#ffffff" stroke-width="2">
        <rect x="75" y="607" width="10" height="10"/>
        <rect x="155" y="631" width="10" height="10"/>
        <rect x="235" y="555" width="10" height="10"/>
        <rect x="315" y="580" width="10" height="10"/>
        <rect x="395" y="500" width="10" height="10"/>
      </g>
    </svg>

    <header class="cover-text">
      <p class="author-name">Author Name</p>
      <h1 class="book-title">
        <span class="title-lead">Mapping of</span>
        <span class="title-main">Tidal Echo Patterns:</span>
        <span class="title-subtitle">Lantern Methods for Quiet Signal Review</span>
      </h1>
    </header>
  </section>
</main>
</body>
</html>
```